Investor Information Presentation Design Required and Corporate overview design

I have all the materials ready to go, just need 1x Pro Design for the presentation and 1x Pro Design for the corporate overview.
I am ok with images being changed (only if it represents the company better). Wording Can NOT be changed. Any process diagrams can be changed to better represent the process.
I can provide high res Logo file and obviously the files for the presentation and corporate overview. What I have done is basic, but need it to look far more polished and professional.

Target Market(s)

Fixed Term Deposits - $100,000 + High interest rates

Industry/Entity Type

Investment

Font styles to use
Sans Serif

Requirements
Must have
• A corporate professional look, think banks, financial services, business etc
• The presentation is NOT used for group presenting purposes - Individuals go through it on their own. Should want to make me feel like I have to read it all!

```html
<!DOCTYPE html>
<html lang="en">
<head>
<meta charset="utf-8">
<title>Meridian Crest Capital – Corporate Overview</title>
<link rel="stylesheet" href="https://fonts.googleapis.com/css2?family=Open+Sans:wght@400;600;700;800&family=Montserrat:wght@600;700&display=swap">
<style>
:root{
  --bg:#d4d5d8;
  --paper:#ffffff;
  --blue:#2b83d0;
  --navy:#1d2c78;
  --indigo:#3b3f9e;
  --violet:#6a5bb5;
  --lilac:#8b83c4;
  --ink:#444a55;
  --muted:#8a8f98;
  --rule:#d9dde3;
}
*{box-sizing:border-box;margin:0;padding:0}
html,body{width:864px;height:1200px;overflow:hidden;background:var(--bg)}
body{position:relative;font-family:"Open Sans",Arial,sans-serif;color:var(--ink)}
.slide{position:absolute;width:270px;height:161px;background:var(--paper);overflow:hidden;box-shadow:0 1px 3px rgba(0,0,0,.25)}
.c1{left:18px}.c2{left:297px}.c3{left:576px}
.r1{top:18px}.r2{top:186px}.r3{top:354px}.r4{top:522px}.r5{top:690px}.r6{top:858px}.r7{top:1026px}
.title{position:absolute;font-family:"Montserrat",Arial,sans-serif;font-weight:600;font-size:9px;color:var(--navy);text-align:center;letter-spacing:.2px}
.title b{color:var(--blue);font-weight:600}
.title::after{content:"";display:block;width:34px;height:1px;background:var(--blue);margin:2px auto 0}
.title.light{color:#fff}
.title.light::after{background:#fff}
.p{position:absolute;font-size:3.6px;line-height:4.6px;color:var(--ink)}
.p em{font-style:normal;color:var(--blue)}
.p.light{color:#e6ecf7}
.h{font-weight:700;color:var(--navy);font-size:4px}
.lead{font-size:4.6px;line-height:5.8px}
.photo{position:absolute}
.foot-mark{position:absolute;left:8px;bottom:5px;display:flex;align-items:center;gap:2px;font-size:3.4px;font-weight:700;color:var(--navy)}
.foot-mark i{display:block;width:4px;height:4px;background:var(--blue)}
.pg{position:absolute;right:8px;bottom:4px;width:8px;height:8px;border-radius:50%;background:var(--indigo);color:#fff;font-size:3.5px;line-height:8px;text-align:center;font-weight:700}
.badge{position:absolute;width:12px;height:12px;border-radius:50%;background:var(--blue);color:#fff;border:1px solid #fff;font-size:4px;line-height:10px;text-align:center;font-weight:700;left:50%;margin-left:-6px}
/* cover */
.cover .brand{position:absolute;left:14px;top:14px;display:flex;align-items:center;gap:4px;font-size:8px;font-weight:700;color:#fff}
.cover .brand i{display:block;width:9px;height:9px;border-radius:50%;background:#fff}
.cover h1{position:absolute;left:14px;top:32px;font-family:"Montserrat",Arial,sans-serif;font-size:11px;font-weight:700;color:#fff;letter-spacing:.3px}
.cover .sub{position:absolute;left:14px;top:46px;font-size:6px;color:#cfe0f6}
.cover .co{position:absolute;left:14px;top:56px;font-size:3.8px;font-weight:700;color:#fff;line-height:4.8px}
.cover .addr{position:absolute;left:14px;right:14px;top:120px;display:flex;justify-content:space-between;font-size:3px;line-height:3.8px;color:#fff}
.cover .addr b{display:block}
.cover .disc{position:absolute;left:14px;right:14px;top:134px;font-size:2.6px;line-height:3.3px;color:#dfe8f7}
.cover.white .brand,.cover.white h1,.cover.white .co,.cover.white .addr{color:var(--navy)}
.cover.white .brand i{background:var(--blue)}
.cover.white .sub,.cover.white .disc{color:var(--ink)}
.ghost{position:absolute;right:20px;top:10px;width:90px;height:90px;border-radius:50%;background:rgba(255,255,255,.06)}
.white .ghost{background:#f1f3f8}
/* partner frame */
.partner{position:absolute;left:18px;top:44px;width:72px;height:62px;border:1px solid var(--rule);display:flex;align-items:center;justify-content:center}
.partner i{display:block;width:22px;height:22px;background:var(--blue)}
/* key points */
.kp{position:absolute;top:42px;left:8px;right:8px;height:100px;display:flex;gap:3px}
.kp div{flex:1;color:#fff;font-size:2.9px;line-height:3.7px;padding:14px 3px 3px;position:relative;text-align:center}
.kp div::before{content:"";position:absolute;top:4px;left:50%;margin-left:-3px;width:6px;height:6px;border:1px solid #fff;border-radius:50%}
.kp b{display:block;font-size:3.2px}
/* objectives */
.obj{position:absolute;left:152px;width:108px;display:flex;gap:3px;align-items:flex-start;font-size:3.4px;line-height:4.2px}
.obj span{flex:none;width:9px;height:8px;background:var(--blue);color:#fff;font-size:3.4px;line-height:8px;text-align:center;font-weight:700}
/* systems */
.sys{position:absolute;left:8px;right:8px;top:34px;height:100px;display:grid;grid-template-columns:repeat(5,1fr);grid-template-rows:1fr 1fr;gap:0}
.sys div{font-size:2.8px;line-height:3.5px;color:#fff;padding:5px 3px;text-align:center}
.sys b{display:block;font-size:3.3px;margin-bottom:1px}
.sys .lt{background:#eef1f6}
.sys .bl{background:var(--blue)}
.sys .nv{background:var(--navy)}
.sys .ic{display:flex;align-items:center;justify-content:center}
/* team */
.region{position:absolute;display:flex;align-items:center;gap:3px;font-size:4px;font-weight:700;color:var(--navy);text-transform:uppercase}
.region i{display:block;width:7px;height:6px;background:var(--blue)}
.member{position:absolute;width:48px;display:flex;gap:2px}
.member .av{flex:none;width:10px;height:10px;border-radius:50%;background:#9aa1ab}
.member p{font-size:2.6px;line-height:3.2px;color:var(--ink)}
.member p b{display:block;color:var(--blue);font-size:2.8px}
/* fx */
.fx{position:absolute;top:100px;width:118px;font-size:3.6px;line-height:4.8px}
.fx b{color:var(--blue);display:block;font-size:4px}
/* contact */
.dir{position:absolute;left:10px;right:10px;top:30px;display:grid;grid-template-columns:repeat(3,1fr);row-gap:9px;column-gap:6px}
.dir p{font-size:3px;line-height:3.9px;color:#fff}
.dir p b{display:block;color:#d5e3f7}
</style>
</head>
<body>

<!-- Row 1: covers -->
<section class="slide cover c1 r1" style="background:linear-gradient(120deg,#2a8ad6,#203f96 60%,#1c2a70)">
  <div class="ghost"></div>
  <div class="brand"><i></i>Meridian Crest Capital</div>
  <h1>CORPORATE OVERVIEW</h1>
  <div class="sub">Commercial in Confidence</div>
  <div class="co">Meridian Crest Capital Pty Ltd<br>ACN: 000 000 000</div>
  <div class="addr"><div><b>Head Office</b>Suite 800, 12 Harbour Lane,<br>Southbank, Victoria 3000</div><div><b>Registered Office Address</b>Level 4, 90 Queen Street,<br>Melbourne, Victoria 3000</div><div><b>Postal Address</b>PO Box 1000</div></div>
  <div class="disc">Disclaimer: This document is confidential and prepared for information only. It does not form an offer and should be read in full together with independent advice before any decision to invest is made.</div>
</section>

<section class="slide cover white c2 r1">
  <div class="ghost"></div>
  <div class="brand"><i></i>Meridian Crest Capital</div>
  <h1>CORPORATE OVERVIEW</h1>
  <div class="sub">Commercial in Confidence</div>
  <div class="co">Meridian Crest Capital Pty Ltd<br>ACN: 000 000 000</div>
  <div class="addr"><div><b>Head Office</b>Suite 800, 12 Harbour Lane,<br>Southbank, Victoria 3000</div><div><b>Registered Office Address</b>Level 4, 90 Queen Street,<br>Melbourne, Victoria 3000</div><div><b>Postal Address</b>PO Box 1000</div></div>
  <div class="disc">Disclaimer: This document is confidential and prepared for information only. It does not form an offer and should be read in full together with independent advice before any decision to invest is made.</div>
</section>

<section class="slide cover c3 r1" role="img" aria-label="Cover with photo of business people reviewing documents in an office, tinted blue" style="background:linear-gradient(110deg,#23469a 0%,#2d5ea8 45%,#55739d 70%,#35405f 100%)">
  <div class="brand"><i></i>Meridian Crest Capital</div>
  <h1>CORPORATE OVERVIEW</h1>
  <div class="sub">Commercial in Confidence</div>
  <div class="co">Meridian Crest Capital Pty Ltd<br>ACN: 000 000 000</div>
  <div class="addr"><div><b>Head Office</b>Suite 800, 12 Harbour Lane,<br>Southbank, Victoria 3000</div><div><b>Registered Office Address</b>Level 4, 90 Queen Street,<br>Melbourne, Victoria 3000</div><div><b>Postal Address</b>PO Box 1000</div></div>
  <div class="disc">Disclaimer: This document is confidential and prepared for information only. It does not form an offer and should be read in full together with independent advice before any decision to invest is made.</div>
</section>

<!-- Row 2 -->
<section class="slide c1 r2">
  <div class="title" style="left:0;right:0;top:16px">Overview</div>
  <div class="partner" role="img" aria-label="Partner company badge"><i></i></div>
  <div class="p" style="left:100px;top:40px;width:150px">Meridian Crest Capital is an <em>innovative investment</em> company that operates in a similar structure to a bank – it sources debt funding from private and corporate lenders to invest in pre-vetted investments that provide a rate of return higher than the cost of borrowing.<br><br>Meridian Crest Capital has access to <em>lucrative investment</em> opportunities due to its relationship with sister company Summit Listing Group (SLG). SLG specialises in helping companies list on stock markets in Australia, and more recently London and New York, and its unique business model attracts investment opportunities not typically open to retail or wholesale investors.<br><br>Meridian Crest Capital currently works with <em>investors in 5 continents</em> who have provided funding to the company in return for a fixed annual rate of return, that is paid quarterly. This simple investment structure provides investors with a steady way of earning a strong rate of return.</div>
  <div class="foot-mark"><i></i>Meridian Crest</div><div class="pg">4</div>
</section>

<section class="slide c2 r2">
  <div class="photo" role="img" aria-label="Photo of a smiling businesswoman in a dark suit" style="left:0;top:0;width:140px;height:161px;background:linear-gradient(160deg,#eef0f2,#c9ccd1 55%,#2d2f36)"></div>
  <div class="title" style="left:140px;right:0;top:16px">Objectives</div>
  <div class="p" style="left:152px;top:42px;font-size:3.8px;font-weight:600;color:var(--navy)">Meridian Crest Capital has 4 key objectives –</div>
  <div class="obj" style="top:54px"><span>01</span>Raise $100m from private and corporate lenders by December 2017</div>
  <div class="obj" style="top:68px"><span>02</span>Provide a flawless service to its investors by always meeting financial commitments</div>
  <div class="obj" style="top:82px"><span>03</span>Execute profitable investments on a consistent basis</div>
  <div class="obj" style="top:96px"><span>04</span>Fill its investor database to participate in other profitable investment opportunities</div>
  <div class="p" style="left:152px;top:114px;width:108px;font-size:2.8px;line-height:3.5px;color:var(--muted)">Each objective is reviewed quarterly by the board to ensure progress is measured and reported to investors.</div>
  <div class="pg">5</div>
</section>

<section class="slide c3 r2">
  <div class="title" style="left:0;right:0;top:16px"><b>Key Points</b> of Difference</div>
  <div class="p" style="left:0;right:0;top:32px;text-align:center;font-weight:600">The key components that make Meridian Crest Capital stand out from other investment companies include –</div>
  <div class="kp">
    <div style="background:var(--blue)"><b>Global Presence</b>Capital raised from investors in Australia, Europe, Asia and North America gives strong stability and a broad reach.</div>
    <div style="background:var(--navy)"><b>Speed</b>Unlike traditional banks, funding decisions are made quickly so that strong opportunities are never missed.</div>
    <div style="background:var(--blue)"><b>Innovation</b>The selection of companies through SLG is a new and unique way to find strong returns.</div>
    <div style="background:var(--indigo)"><b>SLG</b>Its track record in listing companies gives a steady flow of investment opportunities.</div>
    <div style="background:var(--lilac)"><b>Returns</b>Investors receive a higher fixed rate of return than most term deposits, paid every quarter.</div>
  </div>
  <div class="foot-mark"><i></i>Meridian Crest</div><div class="pg">6</div>
</section>

<!-- Row 3 -->
<section class="slide c1 r3">
  <div class="photo" role="img" aria-label="Photo of two businessmen in suits reviewing a document" style="left:0;top:0;width:132px;height:161px;background:linear-gradient(150deg,#f3f4f6,#b8c2cf 50%,#3a4456)"></div>
  <div class="title" style="left:132px;right:0;top:16px"><b>Corporate</b> Structure</div>
  <div class="p" style="left:142px;top:36px;width:118px;font-size:3.2px;line-height:4px">Meridian Crest Capital is a privately company registered with the Australian Securities and Investments Commission. Its registered office is in Melbourne and it is governed by an experienced board of directors.<br><br><b class="h">Meridian Crest Capital USA and UK</b><br>In order to scale up SLG's international presence the company is currently creating joint venture partners in the US and UK to open equivalent companies to assist their local market. The partners sought must have access to a substantial network of investors.<br><br><b class="h">Asset Holding Company</b><br>Meridian Crest Capital is in the process of finalising the setup of an entity that the Australian, US and UK companies will lend investment funds to for the purpose of making investments on behalf of the company.<br><br>This asset holding company will be incorporated in a zero tax jurisdiction and hold the assets of the group, which is separate to the operating entities to provide an added layer of protection to investors.</div>
  <div class="pg">7</div>
</section>

<section class="slide c2 r3">
  <div class="title" style="left:0;right:0;top:16px"><b>Raising</b> Capital</div>
  <div class="p lead" style="left:18px;right:18px;top:36px">Meridian Crest Capital uses a highly effective digital marketing campaign for generating leads from potential investors. This campaign can be turned on/off at any time, and generates an average of $2m worth of investor interest every 24 hours when active.<br><br>Potential investors are qualified by in-house consultants who have been trained on the company's business model such that they can explain the offering to investors and secure funding.<br><br>The company is finding a consistent flow of investment is being received through existing investors inviting others (e.g. family and friends) to be involved.<br><br>In addition to this, it is not uncommon for a large portion of investors to top up their investment after receiving their first quarterly interest payment (i.e. they see proof of concept and are comfortable in investing further money with the company).</div>
  <div class="foot-mark"><i></i>Meridian Crest</div><div class="pg">8</div>
</section>

<section class="slide c3 r3">
  <div class="photo" role="img" aria-label="Photo of a calculator and financial papers on a desk" style="left:0;top:0;width:270px;height:56px;background:linear-gradient(180deg,#4a4f5a,#7c828d 60%,#5b616c)"></div>
  <div class="title light" style="left:0;right:0;top:14px">Investments</div>
  <div class="p light" style="left:0;right:0;top:32px;text-align:center;font-size:3.8px">Meridian Crest Capital is active in 4 categories of investment opportunities as follows –</div>
  <div class="badge" style="top:50px">01</div>
  <div class="p" style="left:12px;right:12px;top:68px"><b class="h" style="color:var(--blue)">1. Bridging Finance</b><br>The company provides short-term funding to companies that are about to undertake a major capital raise, typically listing on a stock exchange. This bridging finance provides working capital to facilitate the process.<br>Bridging loans typically attract 10% per month interest and are repaid from the first funds raised from the listing, usually within 120 days.<br>Clients are required to pay the rate of return as the principal with interest paid out of the largest amount of capital raised, and the loan is secured.<br><br><b class="h">Example</b><br><em>Meridian Crest Capital provided $500,000 to a mobile app client to cover the listing process, which returned $750,000 on completion of the raise, and also a 5% equity stake in the listed company.</em></div>
  <div class="foot-mark"><i></i>Meridian Crest</div><div class="pg">9</div>
</section>

<!-- Row 4 -->
<section class="slide c1 r4">
  <div class="photo" role="img" aria-label="Photo of a stock market chart on a screen" style="left:0;top:0;width:270px;height:56px;background:linear-gradient(180deg,#1c2c4c,#2f5586 60%,#1a2840)"></div>
  <div class="badge" style="top:50px">02</div>
  <div class="p" style="left:12px;right:12px;top:68px"><b class="h" style="color:var(--blue)">2. Pre-IPO Investments</b><br>The company has access to lucrative pre-IPO investment opportunities due to its relationship with SLG. SLG is provided with significant performance fees for its services, which often make it a strong investment proposition.<br>Substantial due diligence is done on such transactions prior to making the investment in order for the client to qualify for funding from Meridian Crest Capital.<br><br><b class="h">Example</b><br><em>SLG invested $175,000 in a technology pre-IPO round which then listed at a 4x multiple, giving a strong return within nine months. The gain was used to fund further opportunities across the group, with profits shared with the holding company.</em></div>
  <div class="foot-mark"><i></i>Meridian Crest</div><div class="pg">10</div>
</section>

<section class="slide c2 r4">
  <div class="photo" role="img" aria-label="Photo of a hand holding a tablet showing a pie chart" style="left:0;top:0;width:270px;height:56px;background:linear-gradient(120deg,#3c3f45,#8c9099 55%,#d5d8dc)"></div>
  <div class="badge" style="top:50px">03</div>
  <div class="p" style="left:12px;right:12px;top:68px"><b class="h" style="color:var(--blue)">3. Short Term Working Capital</b><br>Meridian Crest Capital provides short-term working capital to clients that require funding to grow their businesses. This is typically done in return for either a high rate of interest, typically 15% per annum, and/or shares in the company.<br><br><b class="h">Example</b><br><em>An e-commerce client required an injection of stock capital to meet a large seasonal order. The funds were repaid in full within five months with interest and the client has since returned for a second facility.</em></div>
  <div class="foot-mark"><i></i>Meridian Crest</div><div class="pg">11</div>
</section>

<section class="slide c3 r4">
  <div class="photo" role="img" aria-label="Photo of a hand holding a red credit card over a laptop" style="left:0;top:0;width:270px;height:56px;background:linear-gradient(120deg,#5a5e66,#9aa0a8 50%,#7d2b2f 75%,#4a4e56)"></div>
  <div class="badge" style="top:50px">04</div>
  <div class="p" style="left:12px;right:12px;top:68px"><b class="h" style="color:var(--blue)">4. Asset Purchases</b><br>Meridian Crest Capital and SLG are often approached with fire-sale opportunities to purchase assets distressed and undervalued, including property and other tangible assets, from vendors that urgently need to liquidate their holdings.<br><br><b class="h">Example</b><br><em>A vendor approached the company requiring a quick sale of commercial equipment valued at $800,000. The assets were acquired for $350,000 and resold within three months at market value, delivering a strong profit.</em></div>
  <div class="foot-mark"><i></i>Meridian Crest</div><div class="pg">12</div>
</section>

<!-- Row 5 -->
<section class="slide c1 r5" role="img" aria-label="Slide with photo background of business people in a meeting, tinted dark blue" style="background:linear-gradient(135deg,#1b2350,#253774 50%,#141a3a)">
  <div class="title light" style="left:0;right:0;top:16px">Qualification of Investment Opportunities</div>
  <div class="p light" style="left:14px;right:14px;top:36px;text-align:center;font-weight:600">Meridian Crest Capital often funding to less than 5% of all investment opportunities it is presented with, and when it does choose to provide funding, it does so on terms that are heavily in favour of the company.</div>
  <div class="p light" style="left:14px;top:50px;width:118px"><b>The due diligence procedures undertaken by Meridian Crest Capital and SLG include –</b><br>• Ensuring clients have a clear exit strategy and business plan<br>• Reviewing financial statements and cash flow forecasts<br>• Checks are reviewed against known risk factors and industry benchmarks<br>• Review of the skill and experience of the management team<br>• Review of all material agreements held by the client<br>• Market research into competitors and growth trends</div>
  <div class="p light" style="left:138px;top:58px;width:118px">• Fit for stock exchange listing and compliance requirements<br>• Assessment of legal and regulatory obligations<br>• Independent valuation of assets offered as security<br>• Review of shareholding structure and cap table<br>• Board review of each opportunity before funds released</div>
  <div class="p light" style="left:14px;right:14px;top:112px">A focus is placed on investing solely in businesses which the board understands and is confident can deliver returns. Each investment is monitored monthly and a detailed report is provided to the board until the funds are fully repaid.</div>
  <div class="pg" style="background:#fff;color:var(--navy)">13</div>
</section>

<section class="slide c2 r5">
  <div class="title" style="left:0;right:0;top:8px"><b>Systems</b></div>
  <div class="p" style="left:0;right:0;top:24px;text-align:center;font-weight:600;font-size:3.6px">Meridian Crest Capital currently uses the following systems –</div>
  <div class="sys">
    <div class="lt ic" role="img" aria-label="Illustration of files on a shelf"><svg width="30" height="24" viewBox="0 0 30 24"><rect x="2" y="3" width="7" height="18" fill="#2b83d0"/><rect x="11" y="3" width="7" height="18" fill="#1d2c78"/><rect x="20" y="3" width="7" height="18" fill="#2b83d0"/></svg></div>
    <div class="nv"><b>CRM</b>A custom CRM has been heavily customised to track all investor interactions and funds.</div>
    <div class="lt ic" role="img" aria-label="Illustration of office software tiles"><svg width="30" height="24" viewBox="0 0 30 24"><rect x="3" y="3" width="10" height="8" fill="#2b83d0"/><rect x="16" y="3" width="10" height="8" fill="#6a5bb5"/><rect x="3" y="13" width="10" height="8" fill="#1d2c78"/><rect x="16" y="13" width="10" height="8" fill="#8b83c4"/></svg></div>
    <div class="bl"><b>Email</b>All consultants use a shared email platform with secure access and mobile sync.</div>
    <div class="lt ic" role="img" aria-label="Illustration of an online shop front"><svg width="30" height="24" viewBox="0 0 30 24"><rect x="5" y="6" width="20" height="15" fill="#1d2c78"/><rect x="3" y="3" width="24" height="4" fill="#2b83d0"/></svg></div>
    <div class="bl"><b>Bookkeeping</b>Cloud bookkeeping software records all transactions and monthly accounts.</div>
    <div class="lt ic"><svg width="26" height="26" viewBox="0 0 26 26"><circle cx="13" cy="13" r="10" fill="none" stroke="#1d2c78" stroke-width="2"/><path d="M8 13h10M13 8v10" stroke="#2b83d0" stroke-width="2"/></svg></div>
    <div class="nv"><b>Cloud Workspace</b>A range of cloud tools are used to store and share documents across teams.</div>
    <div class="lt ic"><svg width="26" height="22" viewBox="0 0 26 22"><rect x="2" y="3" width="22" height="16" fill="none" stroke="#2b83d0" stroke-width="2"/><path d="M2 4l11 8 11-8" fill="none" stroke="#2b83d0" stroke-width="2"/></svg></div>
    <div class="nv"><b>Client Portal</b>An online portal lets investors view their accounts and payment history.</div>
  </div>
  <div class="foot-mark"><i></i>Meridian Crest</div><div class="pg">14</div>
</section>

<section class="slide c3 r5">
  <div class="title" style="left:0;right:0;top:16px"><b>Our</b> Team</div>
  <div class="p" style="left:0;right:0;top:32px;text-align:center;font-weight:600">The following team members play an integral role in Meridian Crest Capital's success –</div>
  <div class="region" style="left:12px;top:44px"><i></i>Australia</div>
  <div class="member" style="left:6px;top:58px"><div class="av"></div><p><b>Samir Haddad</b>Managing Partner, Melbourne. Leads investor strategy.</p></div>
  <div class="member" style="left:58px;top:58px"><div class="av"></div><p><b>Nikos Stavrou</b>Investor Relations, Melbourne.</p></div>
  <div class="member" style="left:110px;top:58px"><div class="av"></div><p><b>Helena Brandt</b>Finance Director, oversees all reporting.</p></div>
  <div class="member" style="left:162px;top:58px"><div class="av"></div><p><b>Imran Qureshi</b>Client Services Manager.</p></div>
  <div class="member" style="left:214px;top:58px"><div class="av"></div><p><b>Paolo Ricci</b>Head of Lending Enquiries.</p></div>
  <div class="member" style="left:6px;top:92px"><div class="av"></div><p><b>Grace Lindell</b>Investment Analyst, Melbourne.</p></div>
  <div class="member" style="left:58px;top:92px"><div class="av"></div><p><b>Tom Carver</b>Compliance Officer.</p></div>
  <div class="member" style="left:110px;top:92px"><div class="av"></div><p><b>Ruby Hart</b>Investment Consultant.</p></div>
  <div class="member" style="left:162px;top:92px"><div class="av"></div><p><b>Leo Marsh</b>Marketing Manager.</p></div>
  <div class="member" style="left:214px;top:92px"><div class="av"></div><p><b>Ivy Chen</b>Operations Officer.</p></div>
  <div class="foot-mark"><i></i>Meridian Crest</div><div class="pg">15</div>
</section>

<!-- Row 6 -->
<section class="slide c1 r6">
  <div class="region" style="left:12px;top:18px"><i></i>United Kingdom</div>
  <div class="member" style="left:38px;top:32px;width:66px"><div class="av"></div><p><b>Omar Fielding</b>Managing Director, London office.</p></div>
  <div class="member" style="left:104px;top:32px;width:66px"><div class="av"></div><p><b>Sarah Kemp</b>Investment Manager, London.</p></div>
  <div class="member" style="left:170px;top:32px;width:70px"><div class="av"></div><p><b>Hugo Bell</b>Relationship Manager, London.</p></div>
  <div class="region" style="left:12px;top:80px"><i></i>USA</div>
  <div class="member" style="left:38px;top:96px;width:66px"><div class="av"></div><p><b>Ben Archer</b>Managing Director, New York.</p></div>
  <div class="member" style="left:104px;top:96px;width:66px"><div class="av"></div><p><b>Nina Park</b>Director of Investor Relations.</p></div>
  <div class="member" style="left:170px;top:96px;width:70px"><div class="av"></div><p><b>Cole Rivers</b>Business Development Manager.</p></div>
  <div class="foot-mark"><i></i>Meridian Crest</div><div class="pg">16</div>
</section>

<section class="slide c2 r6">
  <div class="region" style="left:12px;top:12px"><i></i>Canada</div>
  <div class="member" style="left:110px;top:26px;width:70px"><div class="av"></div><p><b>Ethan Moss</b>Sales Director, Toronto.</p></div>
  <div class="region" style="left:12px;top:60px"><i></i>Asia</div>
  <div class="member" style="left:110px;top:74px;width:70px"><div class="av"></div><p><b>Daniel Wong</b>Business Development Manager, Asia.</p></div>
  <div class="region" style="left:12px;top:106px"><i></i>Global</div>
  <div class="member" style="left:70px;top:120px;width:70px"><div class="av"></div><p><b>Claire Dumont</b>Head of Global Investment.</p></div>
  <div class="member" style="left:144px;top:120px;width:70px"><div class="av"></div><p><b>Peter Ashdown</b>Director of Joint Ventures.</p></div>
  <div class="foot-mark"><i></i>Meridian Crest</div><div class="pg">17</div>
</section>

<section class="slide c3 r6">
  <div class="title" style="left:0;right:0;top:18px">Foreign Exchange Partners</div>
  <div class="p lead" style="left:18px;right:18px;top:42px">Meridian Crest Capital has relationships with two foreign exchange brokers who have assisted Meridian Crest Capital lenders with converting their investment into Australian Dollars. Their services can save clients up to 5% on transaction fees as compared to normal banks, which can represent a potential saving of thousands of dollars. We suggest speaking with –</div>
  <div class="fx" style="left:18px"><b>Harbour FX Markets (Sydney)</b>Contact: Alan Pryce<br>Email: alan@harbourfx.example<br>Ph: +61 2 0000 1400<br>Web: www.harbourfx.example</div>
  <div class="fx" style="left:146px;width:110px"><b>Northstar Currency Inc (Ontario)</b>Contact: Lucia Verdi<br>Email: lucia@northstarfx.example<br>Ph: +1 555 010 7330<br>Web: www.northstarfx.example</div>
  <div class="foot-mark"><i></i>Meridian Crest</div><div class="pg">18</div>
</section>

<!-- Row 7 -->
<section class="slide c2 r7" role="img" aria-label="Contact slide with photo background of a business team, tinted blue" style="background:linear-gradient(120deg,#2a7fcd,#3a55a8 50%,#3a3f8f)">
  <div class="title light" style="left:0;right:0;top:12px">Contact Directory</div>
  <div class="dir">
    <p><b>Having an investment (AU or US)</b>Samir Haddad<br>samir@meridiancrest.example<br>+61 400 000 101</p>
    <p><b>Having an investment (UK or Europe)</b>Nikos Stavrou<br>nikos@meridiancrest.example<br>+44 7700 900 102</p>
    <p><b>Finance Queries</b>Helena Brandt<br>helena@meridiancrest.example<br>+61 400 000 103</p>
    <p><b>Customer Service Queries</b>Imran Qureshi<br>imran@meridiancrest.example<br>+61 400 000 104</p>
    <p><b>Listing Enquiries (AU, US &amp; Asia)</b>Paolo Ricci<br>paolo@meridiancrest.example<br>+61 400 000 105</p>
    <p><b>Listing Enquiries (Asia)</b>Daniel Wong<br>daniel@meridiancrest.example<br>+65 8000 0106</p>
    <p><b>Listing Enquiries (UK &amp; Europe)</b>Omar Fielding<br>omar@meridiancrest.example<br>+44 7700 900 107</p>
    <p><b>Seeking Investment</b>Claire Dumont<br>claire@meridiancrest.example<br>+61 400 000 108</p>
    <p><b>US &amp; UK Joint Venture Enquiries</b>Peter Ashdown<br>peter@meridiancrest.example<br>+61 400 000 109</p>
  </div>
  <div class="pg" style="background:#fff;color:var(--navy)">19</div>
</section>

</body>
</html>
```